Luma Vale Hotel Flyer

Design a tri-fold flyer for Luma Vale hotel in western Uganda that will be distributed to tour operators, as well as prospective and current guests. The flyer should highlight the natural serene environment, landscaped gardens, spacious luxurious rooms, local culture and proximity to tourist attractions . The flyer should follow the brand colors and logo in attached guidelines and include some of the text and suphotos provided.

```html
<!DOCTYPE html>
<html lang="en">
<head>
<meta charset="utf-8">
<title>Luma Vale Village – Tri-fold Flyer</title>
<link href="https://fonts.googleapis.com/css2?family=Poppins:wght@400;500;600;700;800&family=Great+Vibes&display=swap" rel="stylesheet">
<style>
  :root{
    --orange:#f15a22;
    --gold:#f4a24a;
    --cream:#f2ebdc;
    --cream-light:#f7f2e7;
    --dark:#221e1d;
    --ink:#2a2524;
    --band:#c8501f;
    --stage:#e6e6e6;
  }
  *{box-sizing:border-box;margin:0;padding:0}
  html,body{width:1200px;height:2759px;overflow:hidden}
  body{background:var(--stage);font-family:'Poppins',sans-serif;color:var(--ink);position:relative}
  .spread{position:absolute;left:50px;width:1100px;height:848px;background:var(--cream);box-shadow:0 6px 24px rgba(0,0,0,.18);overflow:hidden}
  .spread--outside{top:491px}
  .spread--inside{top:1419px}
  .abs{position:absolute}
  .panel-dark{background:var(--dark)}
  .pattern-band{position:absolute;height:14px;background:var(--band)}
  .photo{position:absolute}
  .brand{font-family:'Poppins',sans-serif;font-weight:800;letter-spacing:1px;display:flex;align-items:center;gap:10px;justify-content:center}
  .brand-dot{width:.55em;height:.55em;border-radius:50%;background:var(--orange)}
  /* facilities */
  .facilities-title{left:40px;top:48px;font-weight:800;font-size:29px;line-height:1.12}
  .facilities-title .hl{color:var(--orange)}
  .facilities-list{left:40px;top:162px;width:300px;list-style:none;font-size:13px;line-height:1.25}
  .facilities-list li{position:relative;padding-left:20px;margin-bottom:16px}
  .facilities-list li::before{content:"";position:absolute;left:0;top:4px;width:9px;height:9px;border-radius:50%;border:2.5px solid var(--orange)}
  /* contact */
  .snap{position:absolute;border:5px solid #fff;box-shadow:0 3px 8px rgba(0,0,0,.35)}
  .contact-brand{left:367px;width:366px;top:428px;color:#fff;font-size:34px}
  .contact-ask{left:367px;width:366px;top:492px;text-align:center;font-weight:700;font-size:18px;line-height:1.25}
  .contact-ask .hl{color:var(--orange)}
  .contact-ask .lt{color:var(--cream)}
  .contact-item{left:367px;width:366px;text-align:center;color:#fff;font-size:15px;line-height:1.3}
  .contact-icon{width:26px;height:26px;border-radius:50%;background:var(--orange);display:block;margin:0 auto 10px}
  /* cover */
  .cover-brand{left:733px;width:367px;top:66px;color:var(--dark);font-size:46px}
  .cover-ring{left:770px;top:176px;width:290px;height:290px;border-radius:50%;border:9px solid var(--orange)}
  .cover-script{left:733px;width:367px;top:500px;text-align:center;font-family:'Great Vibes',cursive;font-size:48px;color:var(--dark)}
  .cover-name{left:733px;width:367px;top:548px;text-align:center;font-weight:800;font-size:50px;line-height:1;color:var(--orange)}
  .cover-village{left:733px;width:367px;top:604px;text-align:center;font-weight:800;font-size:50px;line-height:1;color:var(--dark)}
  .cover-sub{left:753px;width:327px;top:676px;text-align:center;font-size:14px;line-height:1.3;font-weight:500}
  .url-banner{position:absolute;height:36px;background:var(--orange);color:#fff;font-weight:700;letter-spacing:3px;font-size:17px;display:flex;align-items:center;justify-content:center;clip-path:polygon(3% 8%,100% 0,97% 50%,100% 100%,2% 92%,0 50%)}
  /* inside */
  .feature-photo{position:absolute;width:122px;height:122px;border-radius:50%;border:4px solid var(--orange)}
  .feature-tag{position:absolute;width:110px;height:22px;border-radius:11px;color:#fff;font-weight:700;font-size:11px;letter-spacing:.5px;display:flex;align-items:center;justify-content:center}
  .tag-orange{background:var(--orange)}
  .tag-dark{background:var(--dark)}
  .feature-text{position:absolute;font-size:11.5px;line-height:1.24;width:150px}
  .divider{position:absolute;border-top:1.5px dashed #9b928a}
  .events-note{left:407px;top:662px;width:318px;font-size:11.5px;line-height:1.24}
  .nature-title{left:898px;top:34px;font-weight:800;font-size:29px;line-height:1.02;color:var(--orange)}
  .nature-sub{left:898px;top:108px;font-weight:700;font-size:15px;line-height:1.25;color:var(--gold)}
  .nature-note{left:898px;top:198px;font-size:13.5px;line-height:1.25;color:#fff}
  .offers-banner{left:770px;top:262px;width:245px;height:30px;background:var(--orange);color:#fff;font-weight:700;font-size:14px;letter-spacing:2px;display:flex;align-items:center;justify-content:center;clip-path:polygon(2% 10%,100% 0,97% 50%,100% 100%,0 92%,3% 50%)}
  .offers-grid{left:770px;top:304px;width:310px;display:grid;grid-template-columns:1fr 1fr;row-gap:10px;column-gap:8px}
  .offer{display:flex;align-items:center;gap:10px;color:#fff;font-size:12.5px;line-height:1.15;height:38px}
  .offer-icon{flex:none;width:36px;height:36px;border-radius:50%;border:2px solid var(--gold);position:relative}
  .offer-icon::after{content:"";position:absolute;inset:8px;border-radius:50%;border:1.5px solid var(--gold)}
  .situated{left:770px;top:506px;width:310px;color:var(--gold);font-weight:700;font-size:13.5px;line-height:1.2}
  .nearby{left:770px;top:552px;width:320px;display:grid;grid-template-columns:1fr 1fr;column-gap:10px;list-style:none;color:#fff;font-size:12.5px;line-height:1.2}
  .nearby li{position:relative;padding-left:18px;margin-bottom:6px}
  .nearby li::before{content:"";position:absolute;left:0;top:4px;width:7px;height:7px;border-radius:50%;border:2px solid var(--orange)}
</style>
</head>
<body>

<!-- Outside spread -->
<section class="spread spread--outside" aria-label="Flyer outside">
  <div class="pattern-band" style="left:0;top:16px;width:367px" role="img" aria-label="Orange tribal border pattern"></div>
  <h2 class="abs facilities-title"><span class="hl">OUR<br>FACILITIES</span><br>INCLUDE</h2>
  <ul class="abs facilities-list">
    <li>A restaurant offering local and western cuisine,</li>
    <li>Events hall and rooms for corporate events<br>and family celebrations</li>
    <li>Lavish rooms in our round stone cottages with spectacular views of the Rwenzori mountains,</li>
    <li>Boutique and shops with the latest designer clothes and souvenirs for family and friends.</li>
    <li>For those who wish to keep up to date with current affairs during their stay, international television channels and internet access are also available.</li>
  </ul>
  <div class="photo" style="left:0;top:500px;width:367px;height:348px;background:linear-gradient(180deg,#3f7fd0 0%,#7fb2e6 35%,#6d7a5e 55%,#5f8a3a 80%,#7c9c3c 100%)" role="img" aria-label="Photo of stone hotel cottages under a blue sky"></div>

  <div class="abs panel-dark" style="left:367px;top:0;width:366px;height:848px"></div>
  <div class="photo" style="left:367px;top:0;width:366px;height:290px;background:linear-gradient(180deg,#9fbad0 0%,#4f7a3a 35%,#7a7670 60%,#4f8a30 100%)" role="img" aria-label="Photo of a round thatched stone cottage among trees"></div>
  <div class="snap" style="left:423px;top:234px;width:125px;height:140px;transform:rotate(-4deg);background:linear-gradient(160deg,#5a8a3a,#b89a6a)" role="img" aria-label="Photo of wicker chairs on a veranda"></div>
  <div class="snap" style="left:548px;top:226px;width:138px;height:146px;transform:rotate(3deg);background:linear-gradient(160deg,#c8c0b0,#b0302a)" role="img" aria-label="Photo of the village craft museum entrance"></div>
  <div class="abs brand contact-brand">LUMA VALE</div>
  <p class="abs contact-ask"><span class="hl">FEEL LIKE HAVING</span><br><span class="lt">THE LUMA VALE EXPERIENCE?</span></p>
  <div class="abs contact-item" style="top:570px">
    <svg class="contact-icon" viewBox="0 0 26 26"><circle cx="13" cy="13" r="13" fill="#f15a22"/><path d="M9 7l3 3-1.5 2a8 8 0 0 0 3.5 3.5l2-1.5 3 3-2 2c-5 0-10-5-10-10z" fill="#fff"/></svg>
    +256 700 123456
  </div>
  <div class="abs contact-item" style="top:640px">
    <svg class="contact-icon" viewBox="0 0 26 26"><circle cx="13" cy="13" r="13" fill="#f15a22"/><rect x="7" y="9" width="12" height="8" fill="#fff"/><path d="M7 9l6 5 6-5" stroke="#f15a22" stroke-width="1.3" fill="none"/></svg>
    LumaValeVillage@mail.com
  </div>
  <div class="abs contact-item" style="top:714px">
    <svg class="contact-icon" viewBox="0 0 26 26"><circle cx="13" cy="13" r="13" fill="#f15a22"/><path d="M13 6a4.5 4.5 0 0 1 4.5 4.5c0 3.5-4.5 8.5-4.5 8.5s-4.5-5-4.5-8.5A4.5 4.5 0 0 1 13 6z" fill="#fff"/><circle cx="13" cy="10.5" r="1.7" fill="#f15a22"/></svg>
    Crater Road 1km from Fort Portal,<br>Fort Portal, Uganda
  </div>

  <div class="abs" style="left:733px;top:0;width:367px;height:848px;background:var(--cream-light)"></div>
  <div class="abs brand cover-brand"><span class="brand-dot"></span>LUMA VALE</div>
  <div class="abs cover-ring" style="background:linear-gradient(160deg,#4f8a3a 0%,#8fb04a 45%,#e8e0c8 60%,#b88a4a 100%)" role="img" aria-label="Photo of a wicker chair on a garden balcony"></div>
  <div class="abs cover-script">Welcome to</div>
  <div class="abs cover-name">LUMA VALE</div>
  <div class="abs cover-village">VILLAGE</div>
  <p class="abs cover-sub">Experience the serenity in luxury accommodation in Fort Portal with beautiful views of Mt. Rwenzori.</p>
  <div class="url-banner" style="left:770px;top:742px;width:290px">www.lumavale.co.ug</div>
  <div class="pattern-band" style="left:733px;top:818px;width:367px" role="img" aria-label="Orange tribal border pattern"></div>
</section>

<!-- Inside spread -->
<section class="spread spread--inside" aria-label="Flyer inside">
  <div class="pattern-band" style="left:0;top:18px;width:733px" role="img" aria-label="Orange tribal border pattern"></div>

  <div class="feature-photo" style="left:43px;top:66px;background:linear-gradient(160deg,#f0ece6,#c8302a)" role="img" aria-label="Photo of a guest room with a red-draped bed"></div>
  <div class="feature-tag tag-orange" style="left:49px;top:193px">ROOMS</div>
  <p class="feature-text" style="left:184px;top:58px">Our luxury rooms are extremely spacious. The ground floor rooms have their own garden and are suitable for families. The upper rooms have glass doors leading to the balcony where you can relax with a glass of wine and enjoy the spectacular views of the Rwenzori mountains,the King's palace and Kijanju village.</p>
  <div class="divider" style="left:43px;top:264px;width:290px"></div>
  <div class="feature-photo" style="left:43px;top:284px;background:linear-gradient(160deg,#d8d0c4,#5a4a3a)" role="img" aria-label="Photo of the restaurant dining area"></div>
  <div class="feature-tag tag-dark" style="left:49px;top:408px">RESTUARANTS</div>
  <p class="feature-text" style="left:184px;top:290px">Savour delicious dishes from local and western menu. We have several dining areas: an inner split level restaurant, intimate upstairs nook, sunny courtyard outside which is ideal during the warm weather, and terrace by the pond with views of nature, surrounding gardens and banana plantation.</p>
  <div class="photo" style="left:0;top:478px;width:367px;height:370px;background:linear-gradient(110deg,#8a1f2a 0%,#3f6a2a 40%,#8a5a3a 60%,#5f8a30 100%)" role="img" aria-label="Photo of the A-frame meditation chapel with stained glass, framed by red foliage"></div>

  <div class="feature-photo" style="left:415px;top:66px;background:linear-gradient(180deg,#e8e4da,#3f6a2a)" role="img" aria-label="Photo of a garden terrace under umbrellas"></div>
  <div class="feature-tag tag-orange" style="left:421px;top:193px">NATURE</div>
  <p class="feature-text" style="left:555px;top:58px">Take a nature tour in Luma Vale's 18 acre grounds through the paddocks and forest and look out for the beautiful birds and monkeys. The herbs and flowers in our gardens are available for sale in our plant nursery. Children and families enjoy the jungle playground which features a zip line.</p>
  <div class="divider" style="left:415px;top:253px;width:300px"></div>
  <div class="feature-photo" style="left:415px;top:275px;background:linear-gradient(180deg,#e8e4da,#3a5a8a,#3f6a2a)" role="img" aria-label="Photo of a cultural dance performance"></div>
  <div class="feature-tag tag-dark" style="left:421px;top:400px">CULTURE</div>
  <p class="feature-text" style="left:555px;top:270px">Experience the melting pot of cultures of the region! We hold cultural performances every Sunday and in 2015, we launched an annual school cultural festival! Buy local crafts from our shops and take a local cultural tour to see how banana beer is made, traditional herbal medicine and see how traditional meals are prepared.</p>
  <div class="divider" style="left:415px;top:482px;width:300px"></div>
  <div class="feature-photo" style="left:415px;top:500px;background:linear-gradient(180deg,#e8e4da,#c8302a,#3f6a2a)" role="img" aria-label="Photo of guests at an outdoor event"></div>
  <div class="feature-tag tag-orange" style="left:421px;top:626px">EVENT</div>
  <p class="feature-text" style="left:555px;top:504px">The events hall, with a capacity of up to 120 people, can be configured for a variety of events from performances, exhibitions, film viewings to corporate and family events. Business facilities and sound equipment are also available.</p>
  <p class="abs events-note">Business facilities and sound equipment are also available. Luma Vale gardens are suitable for outdoor events such as weddings, corporate events and family parties. Cultural performances take place in the gardens every week-end and are open to all our clients.</p>
  <div class="url-banner" style="left:423px;top:766px;width:275px">www.lumavale.co.ug</div>
  <div class="pattern-band" style="left:430px;top:824px;width:303px" role="img" aria-label="Orange tribal border pattern"></div>

  <div class="abs panel-dark" style="left:733px;top:0;width:367px;height:848px"></div>
  <div class="photo" style="left:737px;top:12px;width:155px;height:258px;background:linear-gradient(180deg,#3a3432,#8a6a5a 50%,#c8302a 100%)" role="img" aria-label="Photo of a child on a swing"></div>
  <h2 class="abs nature-title">FEEL THE<br>NATURE</h2>
  <p class="abs nature-sub">Enjoy the Culture,<br>&amp; Live the Life of<br>Uganda</p>
  <p class="abs nature-note">Nestled on 18 acres of<br>beautifully landscaped<br>grounds</p>
  <div class="abs offers-banner">OUR HOTEL OFFERS</div>
  <div class="abs offers-grid">
    <div class="offer"><span class="offer-icon"></span>16 spacious<br>luxury rooms</div>
    <div class="offer"><span class="offer-icon"></span>Serene<br>Gardens</div>
    <div class="offer"><span class="offer-icon"></span>Restaurant</div>
    <div class="offer"><span class="offer-icon"></span>Souvenir<br>Shop</div>
    <div class="offer"><span class="offer-icon"></span>Jungle<br>playground</div>
    <div class="offer"><span class="offer-icon"></span>Meditation<br>Chapel</div>
    <div class="offer"><span class="offer-icon"></span>Nature walks</div>
    <div class="offer"><span class="offer-icon"></span>Cultural<br>performances</div>
  </div>
  <p class="abs situated">Situated close to Fort Portal tourist hub,<br>Luma Vale is ideally located for</p>
  <ul class="abs nearby">
    <li>Birding</li><li>Visits to Hot Springs,</li>
    <li>Hiking</li><li>caves &amp; crater lakes</li>
    <li>Chimpanzee Tracking</li>
  </ul>
  <div class="photo" style="left:733px;top:634px;width:367px;height:214px;background:linear-gradient(180deg,#221e1d 0%,#5a4a40 40%,#e8c830 70%,#c89a5a 100%)" role="img" aria-label="Photo of traditional dancers performing"></div>
</section>

</body>
</html>
```